Marrowby's Vacation Rentals Business Card

Multi Million dollar villa rentals in the Dominican Republic.

Industry/Entity Type

Business

Contact Information for Business Card

I am looking for a high-end look around my company name/logo (see attached) on one side incorporating the following info: first and last name, title, address, phone #, email and company website. On the backside I want to add a full color picture of one of our villas (see attached).

```html
<!DOCTYPE html>
<html lang="en">
<head>
<meta charset="utf-8">
<title>Marrowby's Vacation Rentals – Business Card</title>
<link rel="stylesheet" href="https://fonts.googleapis.com/css2?family=Arimo:wght@400;700&family=Cambo&display=swap">
<style>
  :root {
    --stage: #2e2e2e;
    --card-orange: #f7a631;
    --card-orange-light: #fcbd45;
    --ink: #1b1408;
    --tag-orange: #f9a732;
    --accent-red: #e0422a;
    --sky: #5aa6dc;
    --villa-white: #ece8e0;
    --roof: #c8553a;
    --foliage: #4f6b35;
    --pool: #1aa3e6;
  }
  * { margin: 0; padding: 0; box-sizing: border-box; }
  html, body { width: 1200px; height: 800px; overflow: hidden; }
  body { background: var(--stage); position: relative; font-family: "Arimo", Arial, sans-serif; color: var(--ink); }

  .card { position: absolute; top: 236px; width: 548px; height: 327px; border-radius: 20px; overflow: hidden; }
  .card-back { left: 36px; }
  .villa-photo {
    width: 100%; height: 100%;
    background: linear-gradient(180deg, var(--sky) 0%, var(--villa-white) 18%, var(--villa-white) 38%, var(--roof) 40%, var(--villa-white) 43%, #d9d2c2 60%, var(--foliage) 70%, #e6e2da 80%, var(--pool) 88%, #36b6f0 100%);
  }

  .card-front {
    left: 620px;
    background: radial-gradient(ellipse at 40% 55%, var(--card-orange-light) 0%, var(--card-orange) 70%);
  }
  .divider { position: absolute; left: 268px; top: 50px; width: 1.5px; height: 226px; background: var(--ink); }

  .brand { position: absolute; left: 26px; top: 112px; width: 236px; display: flex; align-items: center; gap: 8px; }
  .brand-dot { width: 26px; height: 26px; border-radius: 50%; background: var(--accent-red); flex: none; }
  .brand-name { font-family: "Cambo", Georgia, serif; color: var(--ink); line-height: 1.05; border-bottom: 1.5px solid var(--ink); padding-bottom: 3px; }
  .brand-name .line1 { display: block; font-size: 30px; }
  .brand-name .line2 { display: block; font-size: 16px; letter-spacing: 0.6px; }

  .person { position: absolute; left: 285px; top: 60px; }
  .person-name { font-size: 18px; letter-spacing: 0.2px; line-height: 1; }
  .person-title { display: inline-flex; align-items: center; margin-top: 4px; }
  .person-title span { background: var(--ink); color: var(--tag-orange); font-size: 16px; padding: 1px 4px; line-height: 1.05; }
  .person-title svg { margin-left: 3px; }

  .contact { position: absolute; left: 285px; font-size: 15px; line-height: 1.3; display: flex; align-items: center; gap: 6px; white-space: nowrap; }
  .contact svg { flex: none; }
  .contact-phone { top: 140px; }
  .contact-email { top: 165px; }
  .contact-address { top: 213px; }
  .contact-web { top: 260px; background: var(--accent-red); color: #fff; padding: 0 4px; border-radius: 2px; gap: 5px; }
  .contact-web::after { content: ""; position: absolute; left: 0; right: 0; bottom: -3px; height: 2px; background: var(--ink); }
</style>
</head>
<body>
  <section class="card card-back">
    <div class="villa-photo" role="img" aria-label="Photo of a white two-storey villa with terracotta roof, arched veranda, sun loungers and a blue swimming pool under palm trees"></div>
  </section>

  <section class="card card-front">
    <div class="brand">
      <div class="brand-dot"></div>
      <div class="brand-name"><span class="line1">Marrowby's</span><span class="line2">VACATION RENTALS</span></div>
    </div>

    <div class="divider"></div>

    <div class="person">
      <div class="person-name">DALE R. WHITMORE</div>
      <div class="person-title">
        <span>Co-Ordinator</span>
        <svg width="24" height="18" viewBox="0 0 24 18"><path d="M5 0h5L5 18H0z M16 0h5l-5 18h-5z" fill="#1b1408"/></svg>
      </div>
    </div>

    <div class="contact contact-phone">
      <svg width="18" height="18" viewBox="0 0 18 18"><rect width="18" height="18" rx="3" fill="#1b1408"/><path d="M5 3.5l2.2 0.4 0.8 2.6-1.4 1.1a7 7 0 0 0 3 3l1.1-1.4 2.6 0.8 0.4 2.2c-1 1.4-3 1.6-5.4 0s-4.4-4-4.6-6.2c-0.1-1.3 0.4-2.1 1.300-2.5z" fill="#f7a631"/></svg>
      <span>512-555-0148</span>
    </div>
    <div class="contact contact-email">
      <svg width="18" height="18" viewBox="0 0 18 18"><rect width="18" height="18" rx="3" fill="#1b1408"/><rect x="3.5" y="5" width="11" height="8" fill="none" stroke="#f7a631" stroke-width="1.4"/><path d="M3.5 5l5.5 4.5 5.5-4.5" fill="none" stroke="#f7a631" stroke-width="1.4"/></svg>
      <span>dale@marrowbys.example</span>
    </div>
    <div class="contact contact-address">
      <svg width="18" height="20" viewBox="0 0 18 20"><rect width="18" height="20" rx="3" fill="#1b1408"/><path d="M9 3.5a4.5 4.5 0 0 1 4.5 4.5c0 3-4.5 8-4.5 8s-4.5-5-4.5-8A4.5 4.5 0 0 1 9 3.5z" fill="#f7a631"/><circle cx="9" cy="8" r="1.7" fill="#1b1408"/></svg>
      <span>1417 Harlan Lane<br>Millbrook, TX 76500</span>
    </div>
    <div class="contact contact-web">
      <svg width="14" height="14" viewBox="0 0 14 14"><circle cx="7" cy="7" r="6" fill="none" stroke="#fff" stroke-width="1.3"/><path d="M1 7h12M7 1c2.2 2 2.2 10 0 12M7 1c-2.2 2-2.2 10 0 12" fill="none" stroke="#fff" stroke-width="1"/></svg>
      <span>www.marrowbys.example</span>
    </div>
  </section>
</body>
</html>
```